Clara Joy Halden- Lantern Waltz- Autumn/Winter Tour Dates

I need high res A3 Tour poster for print and for social media JPG sharing of tour dates.
Also needed Facebook/Twitter Banner Cover Photos of these dates.
Text Needed Below
Clara Joy Halden
Lantern Waltz
Autumn/Winter Tour Dates
03/09 Ravensby Folk Festival
21/09 Swindon- Calder Theatre
01/10 Hitchin- Brackwell Folk Club
17/10 Bath- The Anvil
20/10 Sheffield- Upper Dale Croquet Club
24/10 Birmingham- Orchard Lamp Cafe
26/10 Glasgow- The Nook and Jar
27/10 Edinburgh - The Marble Parlour
08/11 Capital Reel and Ballad Festival- The Crooked Heron
25/11 Lewes- Tandem Record Shop- Live In Store
02/12 Cambridge- The Quayside
27/01 Lincolnshire- Fenmarsh Theatre
Tickets/Info: www.clarajoyhalden-music.example/gigs
(Quotes/Reviews To Put On)
"Outstanding, rich and expressive."            "Vibrant and Experimental"
**** BdM                                                               **** Tunepaths
"Impressive and Invigorating"                        "Enchanting" Acoustic Wire UK
tBarks

Updates
I cannot read the tour dates on most of the submissions so far. They need to be visible to viewers.
Thank You.
Please also be as creative and inventive as possible- not bland.

Target Market(s)
Music Fans- Folk Acoustic Americana
Industry/Entity Type
Media
Font styles to use
Requirements
Must have
- My photo featured prominently
- Look classy and not tacky or OTT
- Look elegant, wintery and eye catching
- The dates must be very clear to read
- Links to Website:

Nice to have
- Something innovative and not boring in terms of layout design
- Perhaps fading/ misty or wintery

Should not have
- Any colours that do not match

```html
<!DOCTYPE html>
<html lang="en">
<head>
<meta charset="utf-8">
<title>Clara Joy Halden – Lantern Waltz Tour Poster</title>
<link rel="stylesheet" href="https://fonts.googleapis.com/css2?family=Cormorant+Garamond:ital,wght@1,600&family=Raleway:wght@300&family=Tinos:ital,wght@0,700;1,400;1,700&display=swap">
<style>
  :root {
    --page-bg: #e4e4e4;
    --poster-bg: #0b0c10;
    --ink-white: #ffffff;
    --ink-blue: #8fa6d6;
    --band-blue: #3f51a8;
    --band-line: #5a6cc0;
    --mist-pale: #b9bccb;
    --mist-light: #7d8499;
    --mist-mid: #474e66;
    --mist-deep: #232a3e;
    --photo-dark: #0b0c10;
  }
  * { margin: 0; padding: 0; box-sizing: border-box; }
  html, body { width: 1200px; height: 1200px; overflow: hidden; background: var(--page-bg); }
  .poster {
    position: absolute; left: 266px; top: 82px; width: 669px; height: 1035px;
    background: var(--poster-bg); overflow: hidden; color: var(--ink-white);
  }
  .poster__photo {
    position: absolute; left: 0; top: 150px; width: 669px; height: 760px;
    background:
      linear-gradient(to bottom, var(--photo-dark) 0%, rgba(11,12,16,0) 14%, rgba(11,12,16,0) 78%, var(--photo-dark) 100%),
      linear-gradient(to right, rgba(11,12,16,0.85) 0%, rgba(11,12,16,0) 22%, rgba(11,12,16,0) 82%, rgba(11,12,16,0.8) 100%),
      radial-gradient(ellipse 95px 120px at 310px 300px, var(--mist-pale) 0%, rgba(185,188,203,0.55) 45%, transparent 100%),
      radial-gradient(ellipse 190px 260px at 320px 320px, rgba(22,28,48,0.95) 0%, rgba(22,28,48,0.7) 55%, transparent 100%),
      radial-gradient(ellipse 230px 200px at 520px 130px, var(--mist-light) 0%, rgba(125,132,153,0.4) 50%, transparent 100%),
      radial-gradient(ellipse 160px 180px at 110px 220px, rgba(100,108,132,0.7) 0%, transparent 100%),
      radial-gradient(ellipse 200px 160px at 560px 520px, rgba(150,152,168,0.55) 0%, transparent 100%),
      linear-gradient(160deg, var(--mist-mid) 0%, var(--mist-deep) 55%, #151a28 100%);
  }
  .poster__facet { position: absolute; left: 0; top: 0; width: 669px; height: 1035px; pointer-events: none; }
  .title {
    position: absolute; left: 0; width: 100%; top: 34px; text-align: center;
    font-family: "Cormorant Garamond", serif; font-style: italic; font-weight: 600;
    font-size: 78px; line-height: 1; letter-spacing: 1px; padding-left: 20px;
  }
  .subtitle {
    position: absolute; left: 36px; right: 32px; top: 111px;
    display: flex; align-items: center; gap: 18px;
    font-family: "Raleway", sans-serif; font-weight: 300; font-size: 50px;
    color: var(--ink-blue); text-transform: uppercase; white-space: nowrap;
  }
  .subtitle::before, .subtitle::after {
    content: ""; flex: 1; height: 3px; background: var(--ink-white);
  }
  .tour-banner { position: absolute; left: 0; top: 486px; width: 420px; height: 46px; }
  .tour-banner__label {
    position: absolute; left: 22px; top: 7px;
    font-family: "Tinos", serif; font-style: italic; font-weight: 700; font-size: 29px;
  }
  .dates {
    position: absolute; left: 22px; top: 536px; list-style: none;
    font-family: "Tinos", serif; font-style: italic; font-size: 23px; line-height: 27.2px;
    white-space: nowrap; text-shadow: 0 1px 3px rgba(0,0,0,0.7);
  }
  .dates__day { color: var(--ink-blue); }
  .tickets {
    position: absolute; left: 22px; top: 888px;
    font-family: "Tinos", serif; font-weight: 700; font-size: 21px; white-space: nowrap;
  }
  .tickets__label { color: var(--ink-blue); }
  .reviews {
    position: absolute; left: 0; top: 924px; width: 669px; height: 59px;
    background: var(--band-blue);
    border-top: 2px solid var(--poster-bg); box-shadow: 0 -4px 0 -2px var(--band-line), 0 4px 0 -2px var(--band-line);
  }
  .reviews__item {
    position: absolute; font-family: "Tinos", serif; font-style: italic; font-weight: 700;
    font-size: 12.5px; white-space: nowrap;
  }
  .reviews__item::before {
    content: ""; display: inline-block; width: 5px; height: 5px; border-radius: 50%;
    background: var(--ink-white); margin-right: 4px; vertical-align: 2px;
  }
  .social {
    position: absolute; left: 22px; top: 992px; display: flex; gap: 18px;
    font-family: "Tinos", serif; font-weight: 700; font-size: 16px;
  }
  .social__item { display: flex; align-items: center; gap: 6px; }
  .social__dot { width: 20px; height: 20px; border-radius: 50%; background: var(--band-line); }
  .album-badge {
    position: absolute; left: 534px; top: 900px; width: 110px; height: 110px; border-radius: 50%;
    border: 3px solid var(--band-blue); box-shadow: 0 0 0 2px var(--poster-bg);
    background: radial-gradient(circle at 50% 40%, #4a5270 0%, #1d2336 55%, #0b0e18 100%);
  }
</style>
</head>
<body>
<main class="poster">
  <div class="poster__photo" role="img" aria-label="Portrait of the singer in a wire and pearl crown with dark blue eye makeup, set against a misty wintery woodland"></div>
  <svg class="poster__facet" viewBox="0 0 669 1035" aria-hidden="true">
    <polygon points="0,380 0,900 669,900 669,700" fill="rgba(11,12,16,0.35)"/>
  </svg>

  <h1 class="title">Clara Joy Halden</h1>
  <h2 class="subtitle">Lantern Waltz</h2>

  <div class="tour-banner">
    <svg width="420" height="46" viewBox="0 0 420 46" aria-hidden="true">
      <polygon points="0,0 400,0 412,46 0,46" fill="var(--band-blue)"/>
      <polygon points="401,0 406,0 418,46 413,46" fill="var(--ink-blue)"/>
    </svg>
    <span class="tour-banner__label">Autumn/Winter Tour Dates</span>
  </div>

  <ul class="dates">
    <li><span class="dates__day">03/09</span> Ravensby Folk Festival</li>
    <li><span class="dates__day">21/09</span> Swindon- Calder Theatre</li>
    <li><span class="dates__day">01/10</span> Hitchin- Brackwell Folk Club</li>
    <li><span class="dates__day">17/10</span> Bath- The Anvil</li>
    <li><span class="dates__day">20/10</span> Sheffield- Upper Dale Croquet Club</li>
    <li><span class="dates__day">24/10</span> Birmingham- Orchard Lamp Cafe</li>
    <li><span class="dates__day">26/10</span> Glasgow- The Nook and Jar</li>
    <li><span class="dates__day">27/10</span> Edinburgh - The Marble Parlour</li>
    <li><span class="dates__day">08/11</span> Capital Reel and Ballad Festival- The Crooked Heron</li>
    <li><span class="dates__day">25/11</span> Lewes- Tandem Record Shop- Live In Store</li>
    <li><span class="dates__day">02/12</span> Cambridge- The Quayside</li>
    <li><span class="dates__day">27/01</span> Lincolnshire- Fenmarsh Theatre</li>
  </ul>

  <p class="tickets"><span class="tickets__label">Tickets/Info:</span> www.clarajoyhalden-music.example/gigs</p>

  <section class="reviews">
    <p class="reviews__item" style="left:20px; top:8px;">"Vibrant and Experimental" **** Tunepaths</p>
    <p class="reviews__item" style="left:290px; top:8px;">"Impressive and Invigorating" tBarks</p>
    <p class="reviews__item" style="left:20px; top:33px;">"Outstanding and Expressive" **** BdM</p>
    <p class="reviews__item" style="left:290px; top:33px;">"Enchanting" Acoustic Wire UK</p>
  </section>

  <div class="social">
    <span class="social__item"><span class="social__dot"></span>clarajoyhaldenmusic</span>
    <span class="social__item"><span class="social__dot"></span>@clarajoyhalden</span>
  </div>

  <div class="album-badge" role="img" aria-label="Album cover artwork for Lantern Waltz showing the singer in dark blue tones"></div>
</main>
</body>
</html>
```